Velmora Skincare packaging designs

We are need to create packaging for our skincare brand. We need two designs. One for round jars which is for creams/capsules and the second will be for bottles/serums Some products will be larger in size so please ensure the packaging design will work and there isn't a lot white/empty space

Below are the names of some of our products.
Screw-On Top Jar (25 pads- 4 inches wide) - Glint Wipes I Skin Brightening Pads
Pump Bottle (2 oz) - ReVIVANT I Hyaluronic Acid + Vitamin Serum
Pump Bottle (6oz) - The Oat Rinse I Conditioning Face Cleanser
Dropper bottle (1 oz) - Quiet Glow I Hydrating Moisturizer
Cream jar (1.5 oz) - Quiet Glow I Hydrating Moisturizer
Capsules Jar (25 capsules in a jar)- Plume Drop I Moisture + Hydrating Capsules
Capsules Jar (25 capsules in a jar) - Clear Burst I Impurity Capsules

We will also need help with the packing design in terms of layout of the logo, item name, desc, and ingredients on each product.

Target Market(s)

women

Industry/Entity Type

skincare, beauty

Font styles to use
Sans Serif

Colors
E54698
E96AAD
F1A4CE
F9D9EA
FCEFF6

Requirements
Must have
• Pantone color is 2052 CP HEX #DAAFCA (218 , 175 , 202)

```html
<!DOCTYPE html>
<html lang="en">
<head>
<meta charset="UTF-8">
<title>Velmora Skincare Labels</title>
<link rel="stylesheet" href="https://fonts.googleapis.com/css2?family=Montserrat:wght@300;400;500;600&display=swap">
<style>
  :root {
    --ink-pink: #DAAFCA;
    --frame: #1f1f1f;
    --paper: #ffffff;
  }
  * { margin: 0; padding: 0; box-sizing: border-box; }
  html, body {
    width: 1200px;
    height: 1200px;
    overflow: hidden;
    background: var(--paper);
  }
  body {
    font-family: "Montserrat", sans-serif;
    color: var(--ink-pink);
    display: flex;
    align-items: center;
    justify-content: center;
    gap: 80px;
  }
  .label {
    border: 1.5px solid var(--frame);
    background: var(--paper);
    display: flex;
    flex-direction: column;
    align-items: center;
    text-align: center;
  }
  .label--dropper {
    width: 351px;
    height: 537px;
    padding: 48px 0 44px;
    justify-content: space-between;
  }
  .label--capsules {
    width: 439px;
    height: 289px;
    justify-content: center;
  }
  .brand-block {
    display: flex;
    flex-direction: column;
    align-items: center;
  }
  .product-name {
    font-weight: 600;
    font-size: 36px;
    letter-spacing: 0.22em;
    margin-right: -0.22em;
    line-height: 1;
  }
  .label--dropper .product-name { font-size: 38px; }
  .brand-name {
    font-weight: 400;
    font-size: 54px;
    letter-spacing: 0.04em;
    line-height: 1;
  }
  .label--dropper .brand-name { font-size: 60px; }
  .label--capsules .brand-name { margin-top: 22px; }
  .product-desc {
    font-weight: 300;
    font-size: 20px;
    letter-spacing: 0.02em;
    margin-top: 14px;
  }
  .label--dropper .product-desc { font-size: 22px; margin-top: 18px; }
  .label--capsules .product-desc { font-size: 19px; margin-top: 10px; }
  .product-size {
    font-weight: 500;
    font-size: 23px;
  }
  .label--dropper .product-size { font-size: 26px; }
  .label--capsules .product-size { font-size: 18px; font-weight: 600; margin-top: 22px; }
</style>
</head>
<body>
  <section class="label label--dropper">
    <h2 class="product-name">Quiet Glow</h2>
    <div class="brand-block">
      <h1 class="brand-name">VELMORA</h1>
      <p class="product-desc">Hydrating Moisturizer</p>
    </div>
    <p class="product-size">(1 oz)</p>
  </section>

  <section class="label label--capsules">
    <h2 class="product-name">Plume Drop</h2>
    <h1 class="brand-name">VELMORA</h1>
    <p class="product-desc">Moisture + Hydrating Capsules</p>
    <p class="product-size">(25 capsules)</p>
  </section>
</body>
</html>
```